Family Farm Looking for meat label

We have a small farm in Italy with two types of cow "Piemontese" and "Pezzata Rossa Valdostana". We need label ( about 5x5 cm) to put on the boxes and on every single piece of meat.

Target Market(s)

private client

Industry/Entity Type

family farm

Colors

Designer to choose colors to be used in the design.

Requirements
Must have
• to write "Azienda Agricola Il Roveto" and the cow like our cow not differently. the Piemontese breed cow has the typical physical shapes as in the photo. No photo on the label just a drawing o something like that.
Nice to have
• just a one label, clear, fine and clean . Maybe with pastel color or watercolor. We are a small family farm.
Should not have
• no photo, no another type of cow

```html
<!DOCTYPE html>
<html lang="it">
<head>
<meta charset="utf-8">
<title>Azienda Agricola Il Roveto – Etichetta carne</title>
<link href="https://fonts.googleapis.com/css2?family=Fira+Sans+Condensed:wght@500;600&display=swap" rel="stylesheet">
<style>
  :root {
    --page-bg: #ffffff;
    --label-red: #e3262c;
    --label-green: #2fb554;
    --label-white: #ffffff;
    --cow-light: #e9e7e3;
    --cow-dark: #5a5855;
  }
  * { margin: 0; padding: 0; box-sizing: border-box; }
  html, body {
    width: 1200px;
    height: 600px;
    overflow: hidden;
    background: var(--page-bg);
  }
  .canvas {
    position: relative;
    width: 1200px;
    height: 600px;
  }
  .meat-label {
    position: absolute;
    left: 330px;
    top: 30px;
    width: 540px;
    height: 540px;
    background: var(--label-red);
    overflow: hidden;
    font-family: "Fira Sans Condensed", "Arial Narrow", sans-serif;
  }
  .meadow {
    position: absolute;
    inset: 0;
    width: 540px;
    height: 540px;
  }
  .meadow polygon { fill: var(--label-green); }
  .cow-illustration {
    position: absolute;
    left: 262px;
    top: 50px;
    width: 278px;
    height: 474px;
    border-radius: 46% 30% 0 0 / 18% 12% 0 0;
    background: linear-gradient(160deg, var(--cow-light) 0%, #cfccc7 55%, var(--cow-dark) 100%);
  }
  .farm-name {
    position: absolute;
    left: 38px;
    top: 86px;
    color: var(--label-white);
    font-weight: 600;
    font-size: 54px;
    line-height: 50px;
    letter-spacing: 1px;
    text-transform: uppercase;
  }
  .farm-name span { display: block; }
  .brand-name {
    position: absolute;
    left: 38px;
    top: 448px;
    color: var(--label-white);
    font-weight: 600;
    font-size: 37px;
    line-height: 1;
    letter-spacing: 0.5px;
    text-transform: uppercase;
  }
</style>
</head>
<body>
  <main class="canvas">
    <section class="meat-label">
      <svg class="meadow" viewBox="0 0 540 540" aria-hidden="true">
        <polygon points="0,378 14,368 22,374 40,362 48,368 66,357 74,363 92,352 100,358 118,347 126,352 137,343 150,352 160,348 180,358 190,354 210,364 220,360 240,370 250,366 270,375 282,370 296,378 310,372 324,378 338,372 352,378 366,372 380,378 394,372 408,378 422,372 436,378 450,372 464,378 478,372 492,378 506,372 520,378 540,372 540,540 0,540"/>
      </svg>
      <div class="cow-illustration" role="img" aria-label="Disegno in bianco e nero di una mucca di razza Piemontese con corna, vista di fronte"></div>
      <h1 class="farm-name">
        <span>Azienda</span>
        <span>Agricola</span>
        <span>Il</span>
        <span>Roveto</span>
      </h1>
      <p class="brand-name">Il Roveto</p>
    </section>
  </main>
</body>
</html>
```